Etikett für Bierflaschen
Anforderungen:
Bitte entwerfen Sie Etiketten für Bierflaschen (Bügelflaschen), welches man ggf. auch als Logo für eine kleine Hausbrauerei benutzen kann.
Der Bezug zur Region sollte erkennbar sein. (Norddeutschland/Teufelsmoor).
Gut wäre, wenn eine Torfkahn-Zeichnung enthalten wäre.
Im Vorder-Etikett sollte der Name der Brauerei (Kranwieder Hausbrauerei), der Biername (58er) und der Biertyp (Bsp.Pilsener), haltbar bis,Vol% zu sehen sein.
Im hinteren Etikett (Flaschenrückseite) möchte ich das Bier beschreiben und die Inhaltsstoffe angeben. Evtl. könnten auch hier haltbar bis und/oder %vol. stehen. Last but not leased hat die Bügelflasche noch ein Etikett am Hals,
Unternehmensbeschreibung:
Hierbei handelt es sich um eine kleine Hausbrauerei, die noch nicht gegründet ist. Wichtig für den Vertrieb des Bieres ist der Bezug zur Region
Norddeutschland,Teufelsmoor,Torfkahn) Das Bier wird nicht in großen Mengen hergestellt. Vorgesehen sind kleinere Fässer und 1-Liter und 2-Literflaschen.
Zielgruppe:
Von jung bis alt.
Farben, Logo-Favoriten und weitere Anforderungen
Nur eine Idee:
Dunkel-Gelb am Rand (hier könnte der Name der Brauerei geschrieben sein), Der Torfkahn und die Landschaft braun.
Ansonsten hell z.B. grau
Die Bezeichnung des Biertyps könnte man je nach Biertyp in verschiedenen Farben hinterlegen.
Ein Beispiel einer anderen Brauerei (Mit Leuchtturm) ist als Datei beigefügt.
Hallo,
Mit freundlichen Grüßen
die Länge des Halsetiketts soll ca. 7,5cm sein. MfG

```html
<!DOCTYPE html>
<html lang="de">
<head>
<meta charset="utf-8">
<title>Kranwieder Hausbrauerei – 58er Etiketten</title>
<link rel="stylesheet" href="https://fonts.googleapis.com/css2?family=Kurale&display=swap">
<style>
  :root {
    --paper: #ffffff;
    --label-dark: #15181f;
    --label-mid: #1d2330;
    --rim-light: #9db0d4;
    --ribbon-light: #e8edf6;
    --ribbon-mid: #b4c3de;
    --ribbon-edge: #7f95c2;
    --accent-blue: #4d6aa8;
    --text-pale: #c9d3e6;
    --text-soft: #a8b7d5;
    --boat-tone: #6f86b4;
  }
  html, body {
    margin: 0;
    padding: 0;
    width: 1200px;
    height: 599px;
    overflow: hidden;
    background: var(--paper);
  }
  .label-sheet {
    display: block;
    width: 1200px;
    height: 599px;
    font-family: "Kurale", Georgia, serif;
  }
  .brewery-arc { font-size: 25px; letter-spacing: 1px; fill: var(--rim-light); }
  .beer-style-tag { font-size: 36px; font-style: italic; font-weight: bold; fill: var(--accent-blue); }
  .beer-name { font-size: 100px; fill: var(--label-dark); }
  .beer-name--back { font-size: 84px; }
  .beer-type { font-size: 32px; fill: var(--text-soft); }
  .description { font-size: 16.5px; fill: var(--text-pale); }
  .ingredients { font-size: 16.5px; fill: var(--text-pale); }
  .facts { font-size: 14px; font-style: italic; fill: var(--accent-blue); }
  .boat-art { fill: var(--boat-tone); opacity: 0.8; }
</style>
</head>
<body>
<svg class="label-sheet" viewBox="0 0 1200 599" xmlns="http://www.w3.org/2000/svg">
  <defs>
    <linearGradient id="label-body" x1="0" y1="0" x2="0" y2="1">
      <stop offset="0" stop-color="var(--label-dark)"/>
      <stop offset="0.6" stop-color="var(--label-mid)"/>
      <stop offset="0.85" stop-color="#2c3750"/>
      <stop offset="1" stop-color="var(--rim-light)"/>
    </linearGradient>
    <linearGradient id="label-rim" x1="0" y1="0" x2="0" y2="1">
      <stop offset="0" stop-color="#1a1f2a"/>
      <stop offset="0.5" stop-color="#3a4764"/>
      <stop offset="1" stop-color="#c8d4ea"/>
    </linearGradient>
    <linearGradient id="ribbon" x1="0" y1="0" x2="1" y2="0">
      <stop offset="0" stop-color="var(--ribbon-edge)"/>
      <stop offset="0.45" stop-color="var(--ribbon-light)"/>
      <stop offset="0.7" stop-color="var(--ribbon-mid)"/>
      <stop offset="1" stop-color="var(--ribbon-edge)"/>
    </linearGradient>
    <clipPath id="back-clip"><circle cx="910" cy="300" r="243"/></clipPath>
    <path id="brewery-arc-path" d="M 110 300 A 180 180 0 0 1 470 300"/>
  </defs>

  <!-- Front label -->
  <g class="front-label">
    <circle cx="290" cy="300" r="250" fill="url(#label-rim)"/>
    <circle cx="290" cy="300" r="238" fill="url(#label-body)"/>
    <text class="brewery-arc"><textPath href="#brewery-arc-path" startOffset="50%" text-anchor="middle">KRANWIEDER HAUSBRAUEREI</textPath></text>
    <text class="beer-style-tag" x="290" y="246" text-anchor="middle">naturtrüb</text>
    <rect class="boat-art" x="94" y="196" width="70" height="120" rx="6" role="img" aria-label="Torfkahn mit Segel, links"/>
    <rect class="boat-art" x="416" y="196" width="70" height="120" rx="6" role="img" aria-label="Torfkahn mit Segel, rechts"/>
    <path d="M 82 302 Q 290 282 498 302 L 498 410 Q 290 392 82 410 Z" fill="url(#ribbon)"/>
    <text class="beer-name" x="290" y="398" text-anchor="middle">58er</text>
    <text class="beer-type" x="290" y="490" text-anchor="middle">Pilsener</text>
  </g>

  <!-- Back label -->
  <g class="back-label">
    <circle cx="910" cy="300" r="250" fill="url(#label-rim)"/>
    <circle cx="910" cy="300" r="238" fill="url(#label-body)"/>
    <text class="description" text-anchor="middle">
      <tspan x="910" y="180">Dieses untergärige Bier ist handwerklich</tspan>
      <tspan x="910" y="205">gebraut und naturbelassen mit Zutaten</tspan>
      <tspan x="910" y="230">aus der Region. Wertvolle Geschmacks-</tspan>
      <tspan x="910" y="255">und gesundheitsfördernde Inhaltsstoffe</tspan>
      <tspan x="910" y="280">werden nicht ausgefiltert, was dem Bier</tspan>
      <tspan x="910" y="305">sein naturtrübes Aussehen verleiht.</tspan>
    </text>
    <text class="ingredients" x="910" y="342" text-anchor="middle">Zutaten: Wasser, Malz, feiner Hopfen</text>
    <text class="facts" x="910" y="398" text-anchor="middle">Alc. 4.5% - e 1L - best before : 22.04.14</text>
    <g clip-path="url(#back-clip)">
      <rect class="boat-art" x="690" y="342" width="62" height="100" rx="6" role="img" aria-label="Torfkahn mit Segel, links"/>
      <rect class="boat-art" x="1068" y="342" width="62" height="100" rx="6" role="img" aria-label="Torfkahn mit Segel, rechts"/>
      <path d="M 650 432 Q 910 405 1170 432 L 1170 560 L 650 560 Z" fill="url(#ribbon)"/>
    </g>
    <text class="beer-name beer-name--back" x="910" y="515" text-anchor="middle">58er</text>
  </g>
</svg>
</body>
</html>
```